Wandering Past Chronicles - Book Cover Design

I need a cover (front, spine, back) designed for the second edition of the historical book - Wandering Past Chronicles. This book was created to be a more engaging supplementary resource to the dry texts of most middle and high school social studies classrooms. Although comprehensive and exhaustively researched, the book at times uses humor and irony to engage the reader. The cover should reflect this tone.

Book Title: Wandering Past Chronicles
Subtitle: The Legends, Customs and Crossroads of Human Memory and the Local Dilemmas of Our Age
Author: Tobias Holloway
Updates

Project Deadline Extended
Reason: As multiple designers are working on adjustments and I am looking for new, creative ideas, I am extending the deadline five days. Thank you.

Project Deadline Extended
Reason: Artists are still making alterations to suggestions made and I also want to give designers a chance to submit new ideas.

Target Market(s)

Middle School and High School Teachers

Font styles to use
Serif

Colors
ec1f27
ffffff
000000

Requirements
Must have
• 1) See attachment for text for front cover, spine, back cover
• 2) Central, engaging image
Nice to have
• A subtle hint of humor, light tone
• Potentially upside down globe spinning
• Prefer black, red, white color scheme
Should not have
• Cartoonish text, images

```html
<!DOCTYPE html>
<html lang="en">
<head>
<meta charset="utf-8">
<title>Wandering Past Chronicles – Cover</title>
<link rel="stylesheet" href="https://fonts.googleapis.com/css2?family=Jost:wght@400;700&family=Crimson+Text:ital,wght@0,400;0,700;1,400;1,700&display=swap">
<style>
  :root {
    --red: #ec1f27;
    --red-deep: #c8141c;
    --white: #ffffff;
    --black: #000000;
    --sans: "Jost", "Futura", sans-serif;
    --serif: "Crimson Text", "Minion Pro", serif;
  }
  html, body { margin: 0; padding: 0; overflow: hidden; background: var(--white); }
  .canvas { position: relative; width: 1200px; height: 837px; overflow: hidden; background: var(--white); }

  /* Back cover */
  .back {
    position: absolute; left: 28px; top: 24px; width: 559px; height: 786px;
    background:
      repeating-linear-gradient(90deg, rgba(255,255,255,0.05) 0 3px, rgba(0,0,0,0.06) 3px 7px, rgba(255,255,255,0) 7px 12px),
      linear-gradient(90deg, var(--red-deep) 0%, var(--red) 45%, #f03a2e 70%, var(--red-deep) 100%);
    color: var(--white);
  }
  .back-title {
    position: absolute; left: 28px; top: 36px; margin: 0;
    font: 700 27px/1 var(--sans); letter-spacing: 0.5px; color: var(--black); white-space: nowrap;
  }
  .back-title .accent { color: var(--white); }
  .blurb { position: absolute; left: 31px; top: 104px; width: 366px; font-family: var(--serif); }
  .blurb .blurb-lead { margin: 0 0 16px; font-size: 15px; line-height: 20px; text-align: left; }
  .blurb p { margin: 0 0 12px; font-size: 10px; line-height: 13.8px; text-align: justify; }
  .blurb .quote { font-style: italic; font-weight: 700; text-align: left; }
  .back-map {
    position: absolute; left: 55px; top: 496px; width: 470px; height: 240px;
    border-radius: 40% 45% 35% 50%;
    background: radial-gradient(ellipse at 50% 45%, rgba(255,255,255,0.5), rgba(255,255,255,0.2) 55%, rgba(255,255,255,0) 72%);
  }
  .back-band {
    position: absolute; left: 8px; top: 744px; width: 540px; height: 24px; box-sizing: border-box;
    background: var(--black); color: var(--white);
    font: 400 10.4px/24px var(--sans); padding: 0 8px; white-space: nowrap; overflow: hidden;
  }

  /* Spine */
  .spine {
    position: absolute; left: 587px; top: 24px; width: 26px; height: 786px;
    background: var(--white);
  }
  .spine-text { position: absolute; left: 2px; writing-mode: vertical-rl; white-space: nowrap; }
  .spine-title { top: 32px; font: 400 19px/22px var(--sans); color: var(--red); letter-spacing: 0.3px; }
  .spine-edition { top: 390px; font: 400 15px/22px var(--serif); color: var(--black); }
  .spine-author { top: 656px; font: 400 14px/22px var(--serif); color: var(--black); }

  /* Front cover */
  .front {
    position: absolute; left: 613px; top: 24px; width: 561px; height: 786px;
    background:
      repeating-linear-gradient(0deg, rgba(255,255,255,0.025) 0 2px, rgba(0,0,0,0) 2px 26px),
      radial-gradient(ellipse at 60% 50%, #333 0%, #1c1c1c 55%, #080808 100%);
  }
  .front-globe {
    position: absolute; left: 118px; top: 228px; width: 360px; height: 440px;
    border-radius: 50%;
    background:
      radial-gradient(ellipse at 58% 62%, rgba(245,245,245,0.75) 0, rgba(200,200,200,0.45) 22%, rgba(110,110,110,0.25) 48%, rgba(60,60,60,0.12) 66%, rgba(0,0,0,0) 72%),
      radial-gradient(ellipse at 34% 28%, rgba(230,230,230,0.55) 0, rgba(150,150,150,0.2) 20%, rgba(0,0,0,0) 36%);
  }
  .front-title {
    position: absolute; left: 33px; top: 30px; margin: 0;
    font: 700 53px/55px var(--sans); letter-spacing: 1px; color: var(--white);
    text-shadow: 2px 2px 3px rgba(0,0,0,0.7);
  }
  .front-title span { display: block; }
  .front-title .accent { color: var(--red); }
  .front-edition {
    position: absolute; left: 29px; top: 674px; margin: 0;
    font: 700 23px/1 var(--serif); color: var(--red);
  }
  .front-author {
    position: absolute; left: 29px; top: 703px; margin: 0;
    font: 400 21px/1 var(--serif); color: #e8e8e8;
  }
  .front-band {
    position: absolute; left: 29px; top: 746px; width: 506px; height: 22px;
    background: var(--red); color: var(--white);
    font: 700 11px/22px var(--serif); text-align: center; white-space: nowrap;
  }
</style>
</head>
<body>
<div class="canvas">

  <section class="back">
    <h2 class="back-title">WANDERING <span class="accent">PAST</span> CHRONICLES</h2>
    <div class="blurb">
      <p class="blurb-lead">Do you know how we got to here?</p>
      <p>Well, if you’re like 97.4% of the people walking the planet, you haven’t got a clue. Sure, you might know a bit about a couple rivers in Mesopotamia, how Thessalos wandered around Athens asking questions or how Anselm Kettering got ticked off one day and nailed a really long essay to the door of a church. But to be honest (and don’t be embarrassed), you’ve got some gaps.</p>
      <p>Be dense no more. In Wandering Past Chronicles, Tobias Holloway once again takes you through all the major tales, traditions and turning points of world history - not just European history, but WORLD history. You’ll figure out real quick that the West might have had some crowning moments, but for the whole of human history, it’s been the Persians, the Indians, the Chinese, the Muslims or some horse peoples from the steppe that have truly turned us into the clever little creatures we are today.</p>
      <p>And while most world history books fade off once the Cold War comes to a close, this sometimes sardonic tome just gets going. Updated to include contemporary debates over topics such as Brexit, the rise of the Ashen Banner, claims to the South China Sea, the mounting refugee crisis and the controversial presidency of Harlan Voss, this second edition finishes with a distinctively comprehensive look at the 21st century challenges facing nine major regions of today’s world - Africa, Latin America, Japan, China, the Middle East, India, Russia, Europe and the United States.</p>
      <p class="quote">“ Tobias Holloway expertly understands what his audience wants to know, what they need to know. A page-turning account of our proudest achievements and our most colossal bumblings. It’s world history for the rest of us.” - Idris Almaqar</p>
    </div>
    <div class="back-map" role="img" aria-label="Pale world map silhouette across the red background"></div>
    <div class="back-band">today’s world - Africa, Latin America, Japan, China, the Middle East, India, Russia, Europe and the United States</div>
  </section>

  <section class="spine">
    <div class="spine-text spine-title">WANDERING PAST CHRONICLES</div>
    <div class="spine-text spine-edition">Second Edition</div>
    <div class="spine-text spine-author">Tobias Holloway</div>
  </section>

  <section class="front">
    <div class="front-globe" role="img" aria-label="Glowing dotted globe of the Americas spinning inside a dark tunnel"></div>
    <h1 class="front-title">
      <span>WANDERING</span>
      <span class="accent">PAST</span>
      <span>CHRONICLES</span>
    </h1>
    <p class="front-edition">Second Edition</p>
    <p class="front-author">Tobias Holloway</p>
    <div class="front-band">The Legends, Customs and Crossroads of Human Memory and the Local Dilemmas of Our Age</div>
  </section>

</div>
</body>
</html>
```